Aunt's Find Calm - Graphic Pic for Book Cover

I need a BOOK Cover design that has Logo incorporated:
Aunt's Find Calm
Book Size 5x7.

This is a play on the word HIGH - which really is just a feeling people may get when they are out in nature. NOT cartoon looking.

Book Cover Words:
Aunt’s Find Calm: That Edge of the Meadow Glow
PS. No Drugs or Alcohol Needed.

I am writing an inspirational book called Aunt’s Find Calm. It is about hard working, determined mothers with dreams of living the good life while raising successful children along the way. The only problem is that most Mother’s have so many responsibilities that they put upon themselves that sometimes they get stuck in a routine and become fearful of adventure and taking risks. As a result, women lose their sense of freedom and do not take much-needed alone time. Yet, ultimately Mother’s can learn to take a break, which can solve many problems and propel them on to a new trail that may include the high country!
Updates

HI.I am looking forward to your designs!! Added Friday, May 1, 2015

Target Market(s)

Mothers of all ages, from 18 to 80

Logo Text

Aunt's Find Calm

Logo styles of interest
Pictorial/Combination Logo
Colors
f68e4e
f68d4d
faa54b
ffc214
fbed22
f04a50

Requirements
Must have
• Colorful, like sunset colors. Vibrant, Fun...
• Words on it:
• Aunt's Find Calm.
• Edge of the Meadow Glow.
• P.S. No Drugs or Alcohol Needed
Nice to have
• I like the billboard idea with logo in it.
• Road into mountain
• Words on it: Aunt's Find Calm. Edge of the Meadow Glow.
• The book cover, website logo all need to tie together.
Should not have
• Attached are some rough ideas...that I drew up. and a image that might be able to be used.

```html
<!DOCTYPE html>
<html lang="en">
<head>
<meta charset="utf-8">
<title>Aunt's Find Calm — Book Cover</title>
<link rel="stylesheet" href="https://fonts.googleapis.com/css2?family=Playfair+Display:wght@400&family=Libre+Baskerville:ital,wght@0,400;1,400&family=Lato:ital,wght@1,700&display=swap">
<style>
  :root {
    --band: #7b5b55;
    --band-line: #a4857e;
    --paper: #ffffff;
    --title: #3f1212;
    --band-text: #ffffff;
    --ps: #e0242b;
    --photo-a: #f0b58c;
    --photo-b: #c0392b;
    --photo-c: #7a8f6a;
  }
  html, body {
    margin: 0;
    padding: 0;
    overflow: hidden;
    background: var(--paper);
  }
  .cover {
    position: relative;
    width: 857px;
    height: 1200px;
    background: var(--paper);
    overflow: hidden;
  }
  .top-band {
    position: absolute;
    left: 0; top: 0;
    width: 100%;
    height: 108px;
    background: var(--band);
    border-bottom: 4px solid var(--band-line);
    box-sizing: border-box;
    display: flex;
    align-items: center;
    justify-content: center;
  }
  .tagline {
    margin: 0;
    font-family: "Libre Baskerville", Georgia, serif;
    font-size: 38px;
    color: var(--band-text);
  }
  .title {
    margin: 0;
    font-family: "Playfair Display", "Times New Roman", serif;
    font-weight: 400;
    color: var(--title);
  }
  .title-line {
    position: absolute;
    left: 0;
    width: 100%;
    text-align: center;
    line-height: 1;
  }
  .title-first { top: 140px; font-size: 196px; }
  .title-mid { top: 350px; font-size: 64px; letter-spacing: 6px; }
  .title-last { top: 420px; font-size: 220px; }
  .author-photo {
    position: absolute;
    left: 258px; top: 686px;
    width: 340px; height: 246px;
    background: linear-gradient(180deg, var(--photo-c) 0%, var(--photo-a) 45%, var(--photo-b) 100%);
    border-radius: 6px;
  }
  .logo-name {
    position: absolute;
    left: 0; top: 944px;
    width: 100%;
    margin: 0;
    text-align: center;
    font-family: "Libre Baskerville", Georgia, serif;
    font-weight: 400;
    font-size: 32px;
    line-height: 40px;
    color: var(--title);
  }
  .postscript {
    position: absolute;
    left: 0; top: 1000px;
    width: 100%;
    margin: 0;
    text-align: center;
    font-family: "Lato", Arial, sans-serif;
    font-style: italic;
    font-weight: 700;
    font-size: 32px;
    line-height: 40px;
    color: var(--ps);
  }
  .bottom-band {
    position: absolute;
    left: 0; bottom: 0;
    width: 100%;
    height: 114px;
    background: var(--band);
    display: flex;
    align-items: center;
    justify-content: center;
  }
  .byline {
    margin: 0;
    font-family: "Libre Baskerville", Georgia, serif;
    font-size: 50px;
    color: var(--band-text);
  }
</style>
</head>
<body>
  <main class="cover">
    <header class="top-band">
      <p class="tagline">That Edge of the Meadow Glow</p>
    </header>

    <h1 class="title">
      <span class="title-line title-first">Aunt’s</span>
      <span class="title-line title-mid">find</span>
      <span class="title-line title-last">Calm</span>
    </h1>

    <div class="author-photo" role="img" aria-label="Photo of the author in a red scarf, arms spread wide in front of a green mountain and sunset road"></div>

    <p class="logo-name">Aunt's Find Calm</p>

    <p class="postscript">P.S. No Drugs or Alcohol Needed</p>

    <footer class="bottom-band">
      <p class="byline">by Marla Quinn</p>
    </footer>
  </main>
</body>
</html>
```